Roof Plumbing Company needs simple, modern business card using the attached logo and below details:

Dean Halloway
Summit Gutters Pty Ltd
ABN: 58 214 937 062
Phone: 0417 286 531
Email: summitgutters@mailbrook.com
Website: summitgutters.com.au

For all of your metal roof plumbing requirements contact Summit Gutters for an obligation free quote - no job too big or to small!

Industry/Entity Type

Business

Contact Information for Business Card

Dean Halloway
Summit Gutters Pty Ltd
ABN 58 214 937 062
0417 286 531
summitgutters@mailbrook.com
summitgutters.com.au

Requirements
Must have
• Bright eye catching design, professional look

```html
<!DOCTYPE html>
<html lang="en">
<head>
<meta charset="utf-8">
<title>Summit Gutters – Business Card</title>
<link rel="stylesheet" href="https://fonts.googleapis.com/css2?family=Source+Sans+3:wght@400;700&display=swap">
<style>
  :root {
    --backdrop: #ecebe8;
    --card: #ffffff;
    --red: #c0202a;
    --red-deep: #a3141d;
    --grey: #8a8a8c;
    --grey-dark: #4a4a4c;
    --ink: #2b2b2b;
  }
  html, body {
    margin: 0;
    width: 1200px;
    height: 902px;
    overflow: hidden;
    background: var(--backdrop);
  }
  .business-card {
    position: absolute;
    left: 100px;
    top: 165px;
    width: 1000px;
    height: 571px;
    background: var(--card);
    box-shadow: 0 10px 30px rgba(0,0,0,0.18);
    font-family: "Source Sans 3", "Myriad Pro", sans-serif;
    overflow: hidden;
  }
  .card-waves {
    position: absolute;
    inset: 0;
    width: 100%;
    height: 100%;
  }
  .brand-name {
    position: absolute;
    left: 95px;
    top: 215px;
    display: flex;
    align-items: center;
    gap: 16px;
    color: var(--red);
    font-weight: 700;
    font-size: 44px;
    line-height: 1;
    letter-spacing: 0.5px;
  }
  .brand-mark {
    width: 24px;
    height: 24px;
    background: var(--grey-dark);
  }
  .divider {
    position: absolute;
    left: 505px;
    top: 120px;
    width: 2px;
    height: 190px;
    background: linear-gradient(to bottom, rgba(192,32,42,0), var(--red), rgba(192,32,42,0));
  }
  .holder {
    position: absolute;
    left: 545px;
    top: 100px;
  }
  .holder-name {
    margin: 0;
    color: var(--red);
    font-weight: 700;
    font-size: 34px;
    line-height: 1.1;
  }
  .holder-company {
    margin: 2px 0 0;
    color: var(--ink);
    font-size: 25px;
    line-height: 1.2;
  }
  .contact-list {
    list-style: none;
    margin: 30px 0 0;
    padding: 0;
    color: var(--ink);
    font-size: 23px;
    line-height: 1.45;
  }
  .contact-list li {
    display: flex;
    align-items: center;
    gap: 12px;
  }
  .contact-icon {
    width: 18px;
    height: 18px;
    flex: none;
    fill: var(--red);
  }
</style>
</head>
<body>
  <section class="business-card" aria-label="Summit Gutters business card">
    <svg class="card-waves" viewBox="0 0 1000 571" preserveAspectRatio="none" aria-hidden="true">
      <defs>
        <linearGradient id="red-band" x1="0" y1="0" x2="1" y2="0">
          <stop offset="0" stop-color="#c9464d"/>
          <stop offset="0.5" stop-color="#c0202a"/>
          <stop offset="1" stop-color="#b21a23"/>
        </linearGradient>
        <linearGradient id="grey-band" x1="0" y1="0" x2="1" y2="0">
          <stop offset="0" stop-color="#a6a6a8"/>
          <stop offset="0.6" stop-color="#7c7c7e"/>
          <stop offset="1" stop-color="#5e5e60"/>
        </linearGradient>
      </defs>
      <path fill="url(#grey-band)" d="M0,335 C300,435 650,500 1000,492 L1000,516 C650,526 300,465 0,368 Z"/>
      <path fill="url(#red-band)" d="M0,388 C300,484 650,546 1000,536 L1000,571 L0,571 Z"/>
    </svg>

    <div class="brand-name"><span class="brand-mark"></span>Summit Gutters</div>

    <div class="divider"></div>

    <div class="holder">
      <h1 class="holder-name">Dean Halloway</h1>
      <p class="holder-company">Summit Gutters Pty Ltd</p>
      <ul class="contact-list">
        <li>
          <svg class="contact-icon" viewBox="0 0 20 20" aria-hidden="true"><path d="M3 2h2v16H3z M5 3h11l-3 4 3 4H5z"/></svg>
          58 214 937 062
        </li>
        <li>
          <svg class="contact-icon" viewBox="0 0 20 20" aria-hidden="true"><path d="M5 2l3 4-2 2c1 2 3 4 5 5l2-2 4 3-2 3C9 17 3 11 2 5z"/></svg>
          0417 286 531
        </li>
        <li>
          <svg class="contact-icon" viewBox="0 0 20 20" aria-hidden="true"><path d="M10 1a9 9 0 1 0 0.01 0zM10 3c1 1 2 3 2 6H8c0-3 1-5 2-6zM3 9h3c0-2 .5-4 1.5-5.5A7 7 0 0 0 3 9zm14 0a7 7 0 0 0-4.5-5.5C13.5 5 14 7 14 9zM3 11a7 7 0 0 0 4.5 5.5C6.5 15 6 13 6 11zm5 0c0 3 1 5 2 6 1-1 2-3 2-6zm6 0c0 2-.5 4-1.5 5.5A7 7 0 0 0 17 11z"/></svg>
          summitgutters.com.au
        </li>
        <li>
          <svg class="contact-icon" viewBox="0 0 20 20" aria-hidden="true"><path d="M10 1a9 9 0 1 0 5 16.5l-1-1.7A7 7 0 1 1 17 10v1a1.5 1.5 0 0 1-3 0V6h-2v.8A4 4 0 1 0 13 14a3.5 3.5 0 0 0 6-3v-1a9 9 0 0 0-9-9zm0 11a2 2 0 1 1 0-4 2 2 0 0 1 0 4z"/></svg>
          summitgutters@mailbrook.com
        </li>
      </ul>
    </div>
  </section>
</body>
</html>
```